Harbourline Property Rentals

We want a business card that is bold and has clean lines and a striking logo that identifies us, but does not look like a typical real estate agent business card. We are a permanent property rental business in a coastal location in Queensland - Noosa Heads. We would like to incorporate a sky blue, charcoal and white in the design and maybe a pale yellow. we would like the word harbourline to be two tone in colour.

Real Estate

```html
<!DOCTYPE html>
<html lang="en">
<head>
<meta charset="utf-8">
<title>Harbourline Property Rentals – Business Card</title>
<link href="https://fonts.googleapis.com/css2?family=Montserrat:wght@700&family=Open+Sans:wght@400;700&family=Cinzel:wght@400&display=swap" rel="stylesheet">
<style>
  :root {
    --backdrop: #e8e6e3;
    --card-black: #161616;
    --charcoal: #2e2e2e;
    --steel: #7d7d7d;
    --wordmark-grey: #6e6e6e;
    --sky: #3ec9cc;
    --white: #f4f4f4;
  }
  * { margin: 0; padding: 0; box-sizing: border-box; }
  html, body { width: 1200px; height: 786px; overflow: hidden; }
  body {
    background: var(--backdrop);
    position: relative;
    font-family: "Open Sans", Arial, sans-serif;
  }
  .card {
    position: absolute;
    top: 238px;
    width: 540px;
    height: 309px;
    background: var(--card-black);
    overflow: hidden;
    box-shadow: 0 6px 18px rgba(0,0,0,0.18);
  }
  .card--front { left: 40px; }
  .card--back { left: 620px; }

  /* Brand name: one colour, one weight; the second brand tone sits in the plain square beside it */
  .wordmark {
    display: flex;
    align-items: center;
    gap: 12px;
    font-family: "Montserrat", Arial, sans-serif;
    font-weight: 700;
    color: var(--wordmark-grey);
    letter-spacing: 1px;
    white-space: nowrap;
  }
  .wordmark__mark {
    display: block;
    background: var(--sky);
    flex: none;
  }
  .card--front .wordmark {
    position: absolute;
    left: 0; right: 0; top: 128px;
    justify-content: center;
    font-size: 44px;
  }
  .card--front .wordmark__mark { width: 30px; height: 30px; }
  .card--back .wordmark {
    position: absolute;
    right: 24px; top: 32px;
    font-size: 38px;
  }
  .card--back .wordmark__mark { width: 26px; height: 26px; }

  .wave { position: absolute; left: 0; top: 0; }

  .identity {
    position: absolute;
    right: 262px; top: 100px;
    text-align: right;
    color: var(--white);
  }
  .identity__name {
    font-weight: 700;
    font-size: 20px;
    color: var(--sky);
    white-space: nowrap;
    margin-bottom: 4px;
  }
  .identity__line { font-size: 12.5px; line-height: 18px; white-space: nowrap; }

  .divider {
    position: absolute;
    left: 290px; top: 108px;
    width: 1px; height: 104px;
    background: var(--steel);
  }

  .contacts {
    position: absolute;
    left: 302px; top: 108px;
    list-style: none;
    color: var(--white);
    font-size: 13px;
    line-height: 20px;
  }
  .contacts li { display: flex; align-items: center; white-space: nowrap; }
  .contacts svg { width: 10px; height: 10px; margin-right: 6px; fill: var(--white); flex: none; }

  .tagline {
    position: absolute;
    right: 22px; bottom: 6px;
    font-family: "Cinzel", Georgia, serif;
    font-size: 17px;
    color: var(--white);
    letter-spacing: 1px;
  }
</style>
</head>
<body>

  <section class="card card--front" aria-label="Card front">
    <div class="wordmark"><span class="wordmark__mark"></span><span class="wordmark__name">HARBOURLINE</span></div>
  </section>

  <section class="card card--back" aria-label="Card back">
    <svg class="wave" width="540" height="309" viewBox="0 0 540 309">
      <path d="M0 170 C90 178 160 235 300 245 C400 252 480 258 540 262 V309 H0Z" fill="var(--charcoal)"/>
      <path d="M0 196 C100 205 170 252 310 262 C410 268 480 272 540 276" fill="none" stroke="var(--sky)" stroke-width="7"/>
      <path d="M0 205 C100 214 170 262 310 270 C410 276 480 280 540 283 V309 H0Z" fill="var(--steel)"/>
    </svg>

    <div class="wordmark"><span class="wordmark__mark"></span><span class="wordmark__name">HARBOURLINE</span></div>

    <div class="identity">
      <div class="identity__name">Daniel R. Hollis</div>
      <div class="identity__line">Managing Member</div>
      <div class="identity__line">2210 Coastal Parade,</div>
      <div class="identity__line">Noosa Heads, QLD 4567</div>
    </div>

    <div class="divider"></div>

    <ul class="contacts">
      <li><svg viewBox="0 0 10 10"><path d="M2 0.5 L3.6 0.5 L4.2 3 L3 3.8 C3.6 5.2 4.8 6.4 6.2 7 L7 5.8 L9.5 6.4 V8 C9.5 9 8.8 9.5 8 9.5 C3.8 9.2 0.8 6.2 0.5 2 C0.5 1.2 1 0.5 2 0.5Z"/></svg>(555) 214-7730</li>
      <li><svg viewBox="0 0 10 10"><rect x="2.5" y="0.5" width="5" height="3"/><rect x="0.5" y="3.5" width="9" height="4.5" rx="1"/><rect x="2.5" y="6.5" width="5" height="3"/></svg>(555) 214-7731</li>
      <li><svg viewBox="0 0 10 10"><path d="M2.5 0 H7.5 A1 1 0 0 1 8.5 1 V9 A1 1 0 0 1 7.5 10 H2.5 A1 1 0 0 1 1.5 9 V1 A1 1 0 0 1 2.5 0Z M2.6 1.2 V8 H7.4 V1.2Z"/></svg>(555) 408-1192</li>
      <li><svg viewBox="0 0 10 10"><path d="M0.5 2 H9.5 V8.5 H0.5Z" /><path d="M0.8 2.3 L5 5.6 L9.2 2.3" fill="none" stroke="var(--card-black)" stroke-width="0.9"/></svg>daniel@harbourlinehomes.com</li>
      <li><svg viewBox="0 0 10 10"><circle cx="5" cy="5" r="4.5" fill="none" stroke="var(--white)" stroke-width="1"/><ellipse cx="5" cy="5" rx="2" ry="4.5" fill="none" stroke="var(--white)" stroke-width="0.9"/><path d="M0.5 5 H9.5" stroke="var(--white)" stroke-width="0.9"/></svg>www.harbourlinehomes.com</li>
    </ul>

    <div class="tagline">Property Rentals</div>
  </section>

</body>
</html>
```